Criação de Papelaria Profissional para Tecnologia & Ciencias
A empresa queria:
" Atuamos no mercado nacional distribuindo conectividade através de Chips M2M, além de Plataforma de Rastreamento Veicular e soluções em IoT. "

```html
<!DOCTYPE html>
<html lang="pt-BR">
<head>
<meta charset="UTF-8">
<title>Vexlo — Cartão de Visita</title>
<link href="https://fonts.googleapis.com/css2?family=Montserrat:wght@400;600;700;800&display=swap" rel="stylesheet">
<style>
  :root {
    --page-bg: #ececec;
    --card-white: #ffffff;
    --brand-black: #1e1c1c;
    --brand-teal: #6fd3bf;
    --text-dark: #2a2a2a;
    --text-white: #ffffff;
  }
  html, body {
    margin: 0;
    padding: 0;
    width: 1200px;
    height: 1200px;
    overflow: hidden;
    background: var(--page-bg);
    font-family: "Montserrat", Arial, sans-serif;
  }
  .business-card {
    position: absolute;
    left: 96px;
    top: 463px;
    width: 1008px;
    height: 250px;
    border-radius: 22px;
    overflow: hidden;
    background: var(--card-white);
    box-shadow: 0 4px 14px rgba(0,0,0,0.12);
  }
  .card-shapes {
    position: absolute;
    inset: 0;
  }
  .brand-block {
    position: absolute;
    left: 0;
    top: 0;
    width: 440px;
    height: 250px;
    display: flex;
    flex-direction: column;
    align-items: center;
    justify-content: center;
    color: var(--text-white);
    padding-left: 60px;
    box-sizing: border-box;
  }
  .brand-name {
    font-weight: 800;
    font-size: 58px;
    letter-spacing: 1px;
    line-height: 1;
    margin-top: 10px;
  }
  .brand-tagline {
    margin-top: 22px;
    font-size: 12px;
    font-weight: 400;
    letter-spacing: 6px;
    text-align: center;
    line-height: 1.8;
  }
  .contact-block {
    position: absolute;
    left: 546px;
    top: 32px;
    color: var(--text-dark);
  }
  .person-name {
    font-size: 28px;
    font-weight: 600;
    color: var(--brand-teal);
    line-height: 1;
    margin: 0;
  }
  .person-role {
    font-size: 16px;
    font-weight: 700;
    margin: 5px 0 0;
    line-height: 1;
  }
  .contact-list {
    list-style: none;
    margin: 16px 0 0;
    padding: 0;
  }
  .contact-item {
    display: flex;
    align-items: center;
    gap: 14px;
    font-size: 14px;
    line-height: 1.2;
    margin-bottom: 12px;
  }
  .contact-icon {
    width: 20px;
    height: 20px;
    flex-shrink: 0;
    fill: var(--brand-teal);
  }
  .contact-item strong { font-weight: 700; }
</style>
</head>
<body>
  <div class="business-card">
    <svg class="card-shapes" width="1008" height="250" viewBox="0 0 1008 250" aria-hidden="true">
      <path d="M0 0 H470 C432 70 428 170 452 250 H0 Z" fill="var(--brand-black)"/>
      <path d="M476 0 H512 C462 70 452 170 476 250 H458 C434 170 440 70 476 0 Z" fill="var(--brand-teal)"/>
      <path d="M450 60 C432 110 432 170 446 230" stroke="var(--brand-teal)" stroke-width="3" fill="none"/>
    </svg>

    <div class="brand-block">
      <div class="brand-name">Vexlo</div>
      <div class="brand-tagline">CONEXÕES<br>INTELIGENTES</div>
    </div>

    <div class="contact-block">
      <h1 class="person-name">NOME COMPLETO</h1>
      <p class="person-role">CARGO OU FUNÇÃO</p>
      <ul class="contact-list">
        <li class="contact-item">
          <svg class="contact-icon" viewBox="0 0 24 24"><path d="M6.6 10.8a15 15 0 0 0 6.6 6.6l2.2-2.2a1 1 0 0 1 1-.25 11.4 11.4 0 0 0 3.6.57 1 1 0 0 1 1 1V20a1 1 0 0 1-1 1A17 17 0 0 1 3 4a1 1 0 0 1 1-1h3.5a1 1 0 0 1 1 1c0 1.25.2 2.45.57 3.57a1 1 0 0 1-.25 1z"/></svg>
          <span>00 0000.00000<br>00 0000.00000</span>
        </li>
        <li class="contact-item">
          <svg class="contact-icon" viewBox="0 0 24 24"><circle cx="12" cy="12" r="10"/><path d="M2 12h20M12 2c3 3 3 17 0 20M12 2c-3 3-3 17 0 20" stroke="#fff" stroke-width="1.4" fill="none"/></svg>
          <span><strong>exemplo-conexoes</strong>.com.br<br><strong>contato</strong>@exemplo-conexoes.com.br</span>
        </li>
        <li class="contact-item">
          <svg class="contact-icon" viewBox="0 0 24 24"><path d="M12 2a7 7 0 0 0-7 7c0 5 7 13 7 13s7-8 7-13a7 7 0 0 0-7-7zm0 9.5A2.5 2.5 0 1 1 12 6.5a2.5 2.5 0 0 1 0 5z"/></svg>
          <span>Nome da <strong>rua, 000</strong> - bairro<br><strong>cidade</strong> - estado - <strong>cep</strong> e país</span>
        </li>
      </ul>
    </div>
  </div>
</body>
</html>
```